LAYOUT design - home page for a NZ winery - needs to be modern design

- This is for a layout design of the home page only. No coding required.

- The design should be based around the attached HPID (home page information design) I've attached both a Word.doc and a PDF - these are the same. The table boxes are just for approximate placement of information – you DON'T have to make it look exactly like this. Information for you is in orange text. Words to go on the design in black text. Most instructions are in the HPID. The only change to the HPID is you can use either the white or grey background logo in the header.

- The design needs to be smart and the colours soft/subtle – lots of space with mainly white and soft grey colours… with just accents/splashes of a soft blue (code: PMS 647) or gold. If you wish to tone down the colours in the photos supplied you could try a design doing this… please don’t all try this! Maybe you could try an RTK watermark from their logo somewhere on the design. Please be creative.

- Expected standard of design examples: (Please DO NOT copy these exactly – they are just examples)
http://www.vantorelwines.example.nz/
http://www.quillbrae.example.nz/
http://www.tessmoorhill.example.com/

Width of content will be 1100 pixels when implemented as a web page. Header height (without nav bar) 150-160 pixels.

The winning PSD file will have to be provided as follows…
1. Canvas size of 2000px x 2000px - 72ppi in Adobe Photoshop (CS5 compatible)
2. Width of content section is 1100px wide - centered in the canvas
3. Any button rollovers/hovers in the PSD as hidden layers.
4. All fonts used must be Google fonts (except for the header fonts).
5. You will need to supply the chosen home page plus one example page (example page as a style guide for how all other pages will look). Example page is only the header and navigational bar at the top, an empty sector in the middle with a column (180 px wide) which can be left or right aligned which means the main sector is 920 pixels wide, and then the footer at the bottom of the page.

Target Market(s)

New Zealand and world market for those who like wine. Upmarket clients.

Colors
ffffff

Requirements
Must have
• clean fresh look with lots of white and soft grey colours.

```html
<!DOCTYPE html>
<html lang="en">
<head>
<meta charset="utf-8">
<title>Ruatara Kiln Estate – Home</title>
<link href="https://fonts.googleapis.com/css2?family=PT+Sans:wght@400;700&family=Great+Vibes&display=swap" rel="stylesheet">
<style>
:root{
  --page:#ededed;
  --header:#d9d9d9;
  --nav:#f4f4f4;
  --ink:#333;
  --muted:#666;
  --accent:#b8361a;
  --link:#3a6fc4;
  --footer:#393939;
  --footer-text:#bdbdbd;
  --footer-bar:#2b2b2b;
  --orange:#d9552a;
}
*{margin:0;padding:0;box-sizing:border-box}
html,body{width:924px;height:1200px;overflow:hidden}
body{position:relative;background:var(--page);font-family:"PT Sans",sans-serif;color:var(--ink)}
.abs{position:absolute}

.site-header{left:0;top:0;width:924px;height:64px;background:linear-gradient(#e3e3e3,#cfcfcf)}
.brand{left:140px;top:4px;width:108px;height:60px;border-radius:54px 54px 0 0;background:#fff;text-align:center;padding-top:22px;font-size:15px;color:#222;letter-spacing:.5px}
.tagline{left:276px;top:20px;font-family:"Great Vibes",cursive;font-size:24px;color:#333}
.social{right:154px;top:14px;display:flex;gap:5px}
.social span,.foot-social span{width:8px;height:8px;border-radius:50%;background:#888;display:block}
.callus{right:154px;top:30px;font-size:11.5px;font-style:italic;color:#333}
.address{right:154px;top:47px;font-size:7.5px;font-style:italic;color:#333}

.main-nav{left:0;top:66px;width:924px;height:31px;background:var(--nav);border-bottom:1px solid #ddd}
.main-nav ul{list-style:none;display:flex;position:absolute;left:140px;top:0;height:31px}
.main-nav li{font-size:9px;line-height:31px;padding:0 6px;color:#222;border-right:1px solid #ddd}
.main-nav li.active{background:#555;color:#fff}

.hero{left:74px;top:97px;width:768px;height:268px;background:linear-gradient(120deg,#5b3a22,#a8744a 45%,#4a2e1a)}
.hero .arrow{top:112px;font-size:38px;color:rgba(255,255,255,.55)}
.dots{left:620px;top:248px;width:89px;height:20px;background:#eee;border-radius:4px 4px 0 0;display:flex;gap:8px;justify-content:center;align-items:center}
.dots i{width:8px;height:8px;border-radius:50%;background:#333;display:block}
.dots i:first-child{background:#fff;border:1px solid #333}

.content-band{left:74px;top:432px;width:768px;height:338px;background:linear-gradient(#d4d4d4,#e9e9e9)}
.slogan{left:69px;top:365px;width:779px;height:67px;background:linear-gradient(#fafafa,#e4e4e4);box-shadow:0 2px 4px rgba(0,0,0,.25);text-align:center}
.slogan h1{font-weight:400;font-size:17px;letter-spacing:1px;margin-top:15px}
.slogan p{font-size:7.5px;color:#555;margin-top:6px}

.tile{width:203px;height:142px;background:#fff;padding:3px;box-shadow:0 1px 3px rgba(0,0,0,.2)}
.tile .ph{width:100%;height:100%;position:relative}
.tile .label{position:absolute;left:0;right:0;bottom:0;height:27px;background:rgba(255,255,255,.3);color:#fff;font-size:12px;text-align:right;padding-right:24px;line-height:27px;text-shadow:0 1px 2px rgba(0,0,0,.6)}

.news{left:0;top:770px;width:924px;height:254px;background:#fbfbfb;border-top:1px solid #ccc}
h2.sec{font-weight:400;font-size:14px;color:var(--accent)}
.news-photo{left:146px;top:803px;width:190px;height:116px;border:1px solid #aaa;padding:2px;background:#fff}
.news-text{left:146px;top:926px;width:192px;font-size:7px;line-height:11px;color:#444;text-align:justify}
.blog{left:360px;top:904px;width:205px}
.blog .more{position:absolute;right:10px;top:5px;font-size:7px;color:var(--link);text-decoration:underline}
.blog ul{list-style:none;margin-top:6px}
.blog li{font-size:6.8px;line-height:9px;color:#444;padding-left:14px;position:relative;margin-bottom:8px}
.blog li::before{content:"";position:absolute;left:3px;top:4px;width:5px;height:5px;border-radius:50%;background:#111}
.promo{width:202px;background:#fff;border:1px solid #ccc;padding:3px}
.club .inner{height:98px;display:flex;background:#f3f6e6}
.club .copy{width:105px;font-size:7.5px;text-align:center;line-height:10px;padding-top:22px}
.club .copy em{font-style:normal;color:#d22}
.club .ph{flex:1;position:relative}
.btn{position:absolute;background:#3a9a2a;color:#fff;font-size:7.5px;font-weight:700;padding:2px 10px;border-radius:2px}
.gift .inner{height:98px;position:relative;color:#fff;text-align:center;font-size:7.5px;line-height:10.5px;padding-top:16px;padding-left:50px;font-weight:700}
.gift .inner b{color:#e23}

.site-footer{left:0;top:1024px;width:924px;height:160px;background:var(--footer);border-top:3px solid var(--orange)}
.site-footer h3{position:absolute;font-size:11.5px;letter-spacing:1px;color:#eee;font-weight:700}
.fcol{top:44px;font-size:7px;line-height:13.8px;color:var(--footer-text);border-right:1px solid #555;height:98px}
.fcol ul{list-style:none}
.contact-rows{left:658px;top:44px;font-size:6.5px;color:var(--footer-text);line-height:8px}
.map{left:664px;top:104px;width:105px;height:35px;border:2px solid #ccc;background:linear-gradient(135deg,#e8e6df,#cfd8e0)}
.foot-social{left:672px;top:148px;display:flex;gap:8px}
.foot-social span{background:var(--orange)}
.footer-bar{left:0;top:1184px;width:924px;height:16px;background:var(--footer-bar);font-size:7px;color:var(--orange);line-height:16px}
</style>
</head>
<body>

<header class="abs site-header"></header>
<div class="abs brand">Ruatara Kiln</div>
<div class="abs tagline">New Zealand's best wine experience</div>
<div class="abs social"><span></span><span></span><span></span><span></span><span></span><span></span></div>
<div class="abs callus">Call us : +64 6 555 0142</div>
<div class="abs address">57, Kowhai Flat Rd, Greytown, New Zealand</div>

<nav class="abs main-nav">
  <ul>
    <li class="active">HOME</li><li>ABOUT US</li><li>BUY WINE</li><li>WINE TOURS</li><li>ACCOMMODATION</li><li>RESTAURANT</li><li>WEDDINGS &amp; EVENTS</li><li>WINE CLUB</li><li>RESOURCE CENTRE</li><li style="border:0">CONTACT</li>
  </ul>
</nav>

<div class="abs hero" role="img" aria-label="Winemaker tasting red wine beside oak barrels in the cellar">
  <span class="abs arrow" style="left:62px">&#8249;</span>
  <span class="abs arrow" style="right:62px">&#8250;</span>
  <div class="abs dots"><i></i><i></i><i></i><i></i></div>
</div>

<div class="abs content-band"></div>
<div class="abs slogan">
  <h1>" COMPANY &nbsp;SLOGAN GOES HERE, WE HAVE THE BEST WINEAROUND"</h1>
  <p>Integer facilisis pharetra risus eget auctor. Nullam viverra dapibus tellus, sit amet cursus turpis vulputate consectetur.</p>
</div>

<div class="abs tile" style="left:134px;top:454px"><div class="ph" role="img" aria-label="Glass of rosé wine" style="background:linear-gradient(135deg,#f3e3d8,#e0806a 60%,#a84030)"><div class="label">BUY WINE</div></div></div>
<div class="abs tile" style="left:355px;top:454px"><div class="ph" role="img" aria-label="Smiling guest on a wine tour" style="background:linear-gradient(135deg,#e8ddd0,#b89a80 55%,#3a4a70)"><div class="label">WINE TOURS</div></div></div>
<div class="abs tile" style="left:580px;top:454px"><div class="ph" role="img" aria-label="Guest cottage among trees and gardens" style="background:linear-gradient(135deg,#5c7a3a,#c8ccc0 50%,#4f6e2c)"><div class="label">ACCOMMODATION</div></div></div>
<div class="abs tile" style="left:134px;top:608px"><div class="ph" role="img" aria-label="Restaurant terrace with red umbrellas" style="background:linear-gradient(135deg,#3c6fc0,#b05a3a 55%,#5a3a20)"><div class="label">RESTAURANT</div></div></div>
<div class="abs tile" style="left:355px;top:608px"><div class="ph" role="img" aria-label="Hot air balloons over vineyard hills at dawn" style="background:linear-gradient(#9cb8d0,#e6d6c0 60%,#6a6050)"><div class="label">WEDDINGS &amp; EVENTS</div></div></div>
<div class="abs tile" style="left:580px;top:608px"><div class="ph" role="img" aria-label="Oak barrels stacked in cellar" style="background:linear-gradient(135deg,#4a2e1c,#b07c50 50%,#3a2214)"><div class="label">RESOURCE CENTRE</div></div></div>

<section class="abs news"></section>
<h2 class="abs sec" style="left:145px;top:781px">What's Happening at RTK...</h2>
<div class="abs news-photo"><div role="img" aria-label="Three wine bottles beside a bunch of grapes" style="width:100%;height:100%;background:linear-gradient(90deg,#6a4a2a,#c83a2a 45%,#e89a8a 65%,#2a3060)"></div></div>
<p class="abs news-text">Exciting times at Ruatara Kiln Estate... we've just revealed our new branding and the website has a fresh new look to reflect this. RTK is looking forward to an eventful and prosperous year so please come and visit us when you're next in the Martin borough region.</p>

<h2 class="abs sec" style="left:360px;top:781px">Social Feed</h2>
<div class="abs blog">
  <h2 class="sec">Wine Blog</h2>
  <span class="more">More &gt;&gt;</span>
  <ul>
    <li>Boutique vineyards excluded from Tasman Air in-flight and airport lounge wine selections...</li>
    <li>No need to take your wine on holiday now!...</li>
    <li>Sheep versus Machines - Who Wins?...</li>
    <li>Boutique vineyards excluded from Tasman Air in-flight and airport lounge wine selections...</li>
  </ul>
</div>

<div class="abs promo club" style="left:581px;top:778px">
  <div class="inner">
    <div class="copy">Join<br>Ruatara Kiln Estate<br>Wine Club today<br>&amp; receive a<br><em>"BUY ONE GET ONE FREE"</em><br>Grape to Glass Wine</div>
    <div class="ph" role="img" aria-label="Guest holding a glass of wine in the vineyard" style="background:linear-gradient(135deg,#c8d0c0,#8a7060 60%,#6a8a50)">
      <span class="btn" style="right:8px;bottom:3px">JOIN US</span>
    </div>
  </div>
</div>
<div class="abs promo gift" style="left:581px;top:892px">
  <div class="inner" role="img" aria-label="Grapes and glasses of red wine" style="background:linear-gradient(90deg,#2a3460,#6a2a2a 60%,#8a1a1a)">
    Give the gift of<br><b>NEW ZEALAND'S BEST WINE</b> experience!<br>Vouchers include accommodation<br>and wine tour options.<br><b>TOUR VOUCHER</b>
    <span class="btn" style="left:72px;bottom:6px;background:#d22">GIFT</span>
  </div>
</div>

<footer class="abs site-footer">
  <h3 style="left:136px;top:14px">IMPORTANT LINKS</h3>
  <h3 style="left:656px;top:14px">CONTACT US</h3>
  <div class="abs fcol" style="left:138px;width:104px"><ul><li>› &nbsp; Home</li><li>› &nbsp; About us</li><li>&nbsp;&nbsp;&nbsp;&nbsp;- The Vineyard &amp; Terroir</li><li>&nbsp;&nbsp;&nbsp;&nbsp;- Winemaking</li><li>&nbsp;&nbsp;&nbsp;&nbsp;- The Team</li><li>&nbsp;&nbsp;&nbsp;&nbsp;- Photos</li><li>&nbsp;&nbsp;&nbsp;&nbsp;- 鲁塔拉酒庄</li></ul></div>
  <div class="abs fcol" style="left:260px;width:90px"><ul><li>› &nbsp; Resource Centre</li><li>&nbsp;&nbsp;&nbsp;- Tasting Notes</li><li>&nbsp;&nbsp;&nbsp;- Image Library</li><li>&nbsp;&nbsp;&nbsp;- Accolades</li><li>&nbsp;&nbsp;&nbsp;- Videos</li><li>&nbsp;&nbsp;&nbsp;- About Us Info</li><li>&nbsp;&nbsp;&nbsp;- Testimonials</li></ul></div>
  <div class="abs fcol" style="left:367px;width:130px"><ul><li>› &nbsp; Buy Wine</li><li>&nbsp;&nbsp;&nbsp;- Our Wines</li><li>&nbsp;&nbsp;&nbsp;- Distribution</li><li>&nbsp;&nbsp;&nbsp;- Online Shop</li><li>&nbsp;&nbsp;&nbsp;- Terms &amp; Conditions</li><li style="margin-top:4px">› &nbsp; Wine Tours</li><li>&nbsp;&nbsp;&nbsp;- Grape to Glass Tour</li><li>&nbsp;&nbsp;&nbsp;- Casual tastings/ Cellar door</li></ul></div>
  <div class="abs fcol" style="left:510px;width:127px"><ul><li>› &nbsp;&nbsp;&nbsp; Accommodation</li><li>&nbsp;&nbsp;&nbsp;&nbsp;&nbsp;&nbsp;- The Winemakers Cottage</li><li>&nbsp;&nbsp;&nbsp;&nbsp;&nbsp;&nbsp;- Packages / Special Offers</li><li style="margin-top:4px">› &nbsp;&nbsp;&nbsp; Restaurant</li><li>› &nbsp;&nbsp;&nbsp; Weddings &amp; Events</li><li>› &nbsp;&nbsp;&nbsp; Wine Club</li></ul></div>
  <div class="abs contact-rows">
    <div style="display:flex"><span style="width:47px">Address:</span><span>Ruatara Kiln Estate<br>57 Kowhai Flat Road<br>Greytown, New<br>Zealand</span></div>
    <div style="display:flex;margin-top:4px"><span style="width:45px">Phone:</span><span>+64 6 555 0142</span></div>
    <div style="display:flex;margin-top:3px"><span style="width:45px">E-mail:</span><span style="color:var(--orange);font-size:5.5px">SUPPORT@EXAMPLE.COM</span></div>
  </div>
  <div class="abs map" role="img" aria-label="Street map showing the estate location">
    <svg class="abs" style="left:46px;top:8px" width="12" height="16" viewBox="0 0 12 16"><path d="M6 0a6 6 0 0 0-6 6c0 4 6 10 6 10s6-6 6-10a6 6 0 0 0-6-6z" fill="#c0271f"/><circle cx="6" cy="6" r="2" fill="#fff"/></svg>
  </div>
  <div class="abs foot-social"><span></span><span></span><span></span><span></span><span></span><span></span></div>
</footer>
<div class="abs footer-bar"><span style="position:absolute;left:142px">© 2014 All rights reserved.</span><span style="position:absolute;right:140px">FAQ / Support / Contacts</span></div>

</body>
</html>
```